Coach/consultant in conflict and challenge needs an enticing flyer

I need a double sided DL flyer design that will describe my work in helping people meet conflict and emotional challenge so they can learn and grow from these difficulties. I want to give a flavour of my style through fresh colours, repeated images used differently (the spiral), and a sense of positivity around conflict and difficulty. I want to attract people who are keen to do things differently and want to engage with creative processes rather than getting stuck in familiar patterns. My work is creative and often includes use of story, images and fables, so I want to convey that as well. I also place the work in a spiritual context, but grounded in practicality so I don't want it to seem New Age or flakey. I want something that seems innovative, professional and intriguing. I've included a sample of something I mocked up in word and also a copy of a flyer for Marla Quennet's Ember Gathering that inspired me to get a DL flyer. I want the design to communicate trust and transformation and engaging with fresh ways of doing things by moving past old habits

Target Market(s)

Mid 30s plus women and men who want to change their approach to conflict and emotional difficulties and are willing to take the creative and challenging journey to do that

Industry/Entity Type

Learn

Colors
acd136
00a990

Requirements
Must have
• a shift in the use of the spiral image,
• use of image of me (Norah)
• bright fresh colours olours that represent growth and transformation--I've suggested lime green as it suggests a sense of growth
• easy to read text
Nice to have
• Interesting non-traditional fonts perhaps text in a contemporary sans serif and another brush script font (like the Ember Gathering example)
• bleed to the edge and run off the page images or text
Should not have
• anything that represents too much tradition or stuckness

```html
<!DOCTYPE html>
<html lang="en">
<head>
<meta charset="utf-8">
<title>Norah Vellacott – DL Flyer</title>
<link href="https://fonts.googleapis.com/css2?family=Poppins:wght@300;500;600&family=Kaushan+Script&display=swap" rel="stylesheet">
<style>
  :root {
    --lime: #9ecd2f;
    --earth: #5a4536;
    --photo-warm: #d8632a;
    --photo-grey: #8f8a84;
  }
  * { margin: 0; padding: 0; box-sizing: border-box; }
  html, body { width: 1200px; height: 600px; overflow: hidden; background: var(--lime); }
  .flyer {
    position: relative; width: 1200px; height: 600px; overflow: hidden;
    background: var(--lime); color: var(--earth);
    font-family: "Poppins", sans-serif;
  }
  .frame, .portrait { position: absolute; inset: 0; }
  .abn {
    position: absolute; left: 22px; top: 18px;
    font-size: 15px; font-weight: 300; letter-spacing: .3px;
    border-bottom: 1px solid var(--earth); padding-bottom: 2px;
  }
  .tilted { position: absolute; transform-origin: left top; transform: rotate(-8.5deg); }
  .intro { left: 64px; top: 140px; width: 740px; }
  .intro p { font-size: 19px; font-weight: 300; line-height: 1.38; margin-bottom: 18px; }
  .services { left: 104px; top: 382px; list-style: none; }
  .services li {
    font-family: "Kaushan Script", cursive; font-size: 35px; line-height: 1;
    margin-bottom: 20px; padding-left: 28px; position: relative;
  }
  .services li::before {
    content: ""; position: absolute; left: 2px; top: 15px;
    width: 11px; height: 11px; border-radius: 50%; background: var(--earth);
  }
  .identity { left: 420px; top: 318px; }
  .identity .name-row { display: flex; align-items: center; gap: 12px; }
  .identity .mark { width: 56px; height: 56px; border-radius: 50%; background: var(--earth); flex: none; }
  .identity .name { font-family: "Kaushan Script", cursive; font-size: 40px; line-height: 1; }
  .identity .credentials { font-size: 13.5px; font-weight: 500; margin-left: 70px; margin-top: -4px; }
  .contacts { left: 484px; top: 398px; list-style: none; }
  .contacts li {
    display: flex; align-items: center; gap: 12px; height: 34px;
    font-size: 19px; font-weight: 600;
  }
  .contacts svg { width: 20px; height: 20px; flex: none; }
  .signature-band {
    font-family: "Kaushan Script", cursive; white-space: nowrap; line-height: 1;
  }
  .signature-band.small { left: 200px; top: 588px; font-size: 64px; }
  .signature-band.large { left: 640px; top: 500px; font-size: 170px; }
</style>
</head>
<body>
<main class="flyer">
  <svg class="portrait" viewBox="0 0 1200 600" role="img" aria-label="Portrait photograph of Norah, smiling, wearing an orange knitted wrap">
    <defs>
      <linearGradient id="portraitTone" x1="0" y1="0" x2="0" y2="1">
        <stop offset="0" stop-color="var(--photo-grey)"/>
        <stop offset=".45" stop-color="#b77a55"/>
        <stop offset="1" stop-color="var(--photo-warm)"/>
      </linearGradient>
    </defs>
    <polygon points="900,0 1200,0 1200,444 880,494 824,400 860,120" fill="url(#portraitTone)"/>
  </svg>

  <svg class="frame" viewBox="0 0 1200 600" aria-hidden="true">
    <g stroke="var(--earth)" stroke-width="4" fill="none">
      <polyline points="40,138 3,144 72,600"/>
      <line x1="792" y1="20" x2="944" y2="0"/>
      <line x1="1144" y1="0" x2="1200" y2="264"/>
      <line x1="216" y1="600" x2="1200" y2="444"/>
    </g>
  </svg>

  <div class="abn">ABN 12 345 678 90</div>

  <section class="intro tilted">
    <p>Consult with Norah to address challenges in your life, relationship, group or organisation. Through listening, conversation and creative processes, you will discover what your challenge is asking of you. Norah Vellacott is a skilled facilitator who works to shift people's responses from reactivity to creativity.</p>
    <p>With many years' experience in coaching and mentorship, mediation and narrative processes, Norah supports you to uncover unique responses to difficult situations.</p>
  </section>

  <ul class="services tilted">
    <li>consultations</li>
    <li>workshops</li>
    <li>speaking</li>
    <li>articles</li>
  </ul>

  <div class="identity tilted">
    <div class="name-row">
      <span class="mark" aria-hidden="true"></span>
      <span class="name">Norah Vellacott</span>
    </div>
    <div class="credentials">PhD, MCR, BAppSci, DipHum, AssDipEd</div>
  </div>

  <ul class="contacts tilted">
    <li>
      <svg viewBox="0 0 20 20" aria-hidden="true"><rect width="20" height="20" rx="4" fill="var(--earth)"/><rect x="7" y="4" width="6" height="12" rx="1.5" fill="none" stroke="var(--lime)" stroke-width="1.6"/></svg>
      0400 555 218
    </li>
    <li>
      <svg viewBox="0 0 20 20" aria-hidden="true"><rect width="20" height="20" rx="4" fill="var(--earth)"/><path d="M5 8c0-2 10-2 10 0v1h-3V8H8v1H5z M6 10h8l1 5H5z" fill="var(--lime)"/></svg>
      +61 3 5550 1842
    </li>
    <li>
      <svg viewBox="0 0 20 20" aria-hidden="true"><rect width="20" height="20" rx="4" fill="var(--earth)"/><rect x="4" y="6" width="12" height="8" fill="none" stroke="var(--lime)" stroke-width="1.5"/><polyline points="4,6 10,11 16,6" fill="none" stroke="var(--lime)" stroke-width="1.5"/></svg>
      norah@norahvellacott.com
    </li>
    <li>
      <svg viewBox="0 0 20 20" aria-hidden="true"><rect width="20" height="20" rx="4" fill="var(--earth)"/><g fill="none" stroke="var(--lime)" stroke-width="1.3"><circle cx="10" cy="10" r="6"/><ellipse cx="10" cy="10" rx="2.6" ry="6"/><line x1="4" y1="10" x2="16" y2="10"/></g></svg>
      norahvellacott.com
    </li>
  </ul>

  <div class="signature-band small tilted" aria-hidden="true">Norah Vellacott</div>
  <div class="signature-band large tilted" aria-hidden="true">Norah Vellacott</div>
</main>
</body>
</html>
```